Business Cards and Stationary for telecommunications application
BrightOak Ventures
Business Cards and Stationary for telecommunications application - Telecommunications
Creative Brief
Simple
Louis Merrow
President
20391 Kelvane Court Larkmoor Springs, WV
louis@brightoakventures.com
brightoakventures.com

```html
<!DOCTYPE html>
<html lang="en">
<head>
<meta charset="utf-8">
<title>BrightOak Ventures – Business Card</title>
<link href="https://fonts.googleapis.com/css2?family=Open+Sans:wght@400;600;700&display=swap" rel="stylesheet">
<style>
  :root {
    --page-bg: #e9e7e4;
    --card-bg: #ffffff;
    --brand-red: #b3161c;
    --ink: #2b2b2b;
    --ink-soft: #3a3a3a;
    --edge-dark: #3b3b3b;
  }
  * { margin: 0; padding: 0; box-sizing: border-box; }
  html, body {
    width: 1200px; height: 902px; overflow: hidden;
    background: var(--page-bg);
    font-family: "Open Sans", Arial, sans-serif;
  }
  .card {
    position: absolute; left: 100px; top: 165px;
    width: 1000px; height: 572px;
    background: var(--card-bg);
    box-shadow: 0 2px 6px rgba(0,0,0,.15);
    overflow: hidden;
  }
  .side-band {
    position: absolute; top: 0; right: 0; width: 50px; height: 100%;
    background: var(--brand-red);
    border-left: 5px solid var(--edge-dark);
  }
  .side-band__url {
    position: absolute; left: 50%; top: 30px;
    transform-origin: left top;
    transform: translateX(9px) rotate(90deg);
    color: #fff; font-size: 17px; font-weight: 600;
    letter-spacing: 1.5px; white-space: nowrap;
  }
  .brand {
    position: absolute; left: 60px; top: 110px;
    display: flex; align-items: center; gap: 18px;
  }
  .brand__mark {
    width: 82px; height: 82px; border-radius: 50%;
    background: var(--ink);
  }
  .brand__name {
    font-size: 44px; font-weight: 600; color: var(--ink);
    letter-spacing: -1px;
  }
  .person {
    position: absolute; left: 60px; top: 310px;
  }
  .person__pointer {
    position: absolute; left: -60px; top: 8px;
    width: 0; height: 0;
    border-top: 16px solid transparent;
    border-bottom: 16px solid transparent;
    border-left: 18px solid var(--edge-dark);
  }
  .person__name {
    font-size: 30px; font-weight: 700; color: var(--brand-red);
    line-height: 1.2;
  }
  .person__title {
    font-size: 26px; font-weight: 400; color: var(--ink);
    line-height: 1.35;
  }
  .contact {
    position: absolute; left: 530px; top: 210px;
    list-style: none;
    font-size: 20px; color: var(--ink-soft);
  }
  .contact__item {
    display: flex; align-items: flex-start; gap: 12px;
    margin-bottom: 8px; line-height: 28px;
  }
  .contact__icon {
    flex: 0 0 22px; width: 22px; height: 22px; margin-top: 3px;
  }
</style>
</head>
<body>
  <div class="card">
    <div class="side-band">
      <span class="side-band__url">www.brightoakventures.com</span>
    </div>

    <div class="brand">
      <span class="brand__mark"></span>
      <span class="brand__name">BrightOak Ventures</span>
    </div>

    <div class="person">
      <span class="person__pointer"></span>
      <p class="person__name">Louis Merrow</p>
      <p class="person__title">President</p>
    </div>

    <ul class="contact">
      <li class="contact__item">
        <svg class="contact__icon" viewBox="0 0 22 22"><path d="M3 11 L11 4 L19 11 M6 9 V18 H16 V9" fill="none" stroke="var(--brand-red)" stroke-width="2.2" stroke-linejoin="round"/></svg>
        <span>20391 Kelvane Court<br>Larkmoor Springs, WV</span>
      </li>
      <li class="contact__item">
        <svg class="contact__icon" viewBox="0 0 22 22"><circle cx="11" cy="11" r="11" fill="var(--brand-red)"/><path d="M7 6 L9 6 L10 9 L8.5 10 Q10 13 12 13.5 L13 12 L16 13 L16 15 Q11 16 7 11 Q6 8 7 6Z" fill="#fff"/></svg>
        <span>303-555-0148</span>
      </li>
      <li class="contact__item">
        <svg class="contact__icon" viewBox="0 0 22 22"><circle cx="11" cy="11" r="11" fill="var(--brand-red)"/><rect x="5" y="7" width="12" height="8" fill="#fff"/><path d="M5 7 L11 12 L17 7" fill="none" stroke="var(--brand-red)" stroke-width="1.3"/></svg>
        <span>louis@brightoakventures.com</span>
      </li>
      <li class="contact__item">
        <svg class="contact__icon" viewBox="0 0 22 22"><circle cx="11" cy="11" r="11" fill="var(--brand-red)"/><circle cx="11" cy="11" r="6" fill="none" stroke="#fff" stroke-width="1.4"/><path d="M5 11 H17 M11 5 Q7.5 11 11 17 M11 5 Q14.5 11 11 17" fill="none" stroke="#fff" stroke-width="1.2"/></svg>
        <span>www.brightoakventures.com</span>
      </li>
    </ul>
  </div>
</body>
</html>
```